Landing page для Детский клуб "Тиливки"
Название сайта (домена, или проекта)
Детский клуб "Тиливки"
Цель: Создать современный одностраничный сайт (лендинг) с возможностью в будущем добавлять внутренние страницы. Основная задача — презентовать клуб, его методику и преподавателей, сформировать образ надежного и профессионального детского центра. Итоговая цель — убедить родителей детей 1-7 лет записать ребенка на пробное занятие.
Целевая аудитория: Родители (преимущественно мамы) детей 1-7 лет в Ижевске, для которых важны качество, безопасность, индивидуальный подход, санитарная обработка материалов и профессионализм педагогов.
Детальное ТЗ, логотип, фотографии (для использования на лэндинге) можно найти по ссылке – https://files.nebolka-cloud.ru/d/kqmrtZa-WPn4LH
Адаптивность сайта
Десктопная версия, Версия для планшетов, Версия для телефонов

```html
<!DOCTYPE html>
<html lang="ru">
<head>
<meta charset="utf-8">
<title>Детский клуб "Тиливки"</title>
<link href="https://fonts.googleapis.com/css2?family=Montserrat:wght@500;600;700&family=Unbounded:wght@700;800&display=swap" rel="stylesheet">
<style>
  :root {
    --yellow: #f2c04a;
    --yellow-deep: #efb63c;
    --sky: #8ec3de;
    --blue-btn: #6fa6dc;
    --blue-text: #5a9fdc;
    --lemon: #f7ea3d;
    --pink: #e0459c;
    --violet: #b14fc7;
    --ink: #2b2b2b;
    --white: #ffffff;
    --logo: #7a4fb0;
  }
  * { margin: 0; padding: 0; box-sizing: border-box; }
  html, body { width: 1200px; height: 915px; overflow: hidden; }
  body { font-family: "Montserrat", sans-serif; color: var(--ink); background: var(--yellow); position: relative; }

  .topbar { position: absolute; left: 0; top: 0; width: 1200px; height: 86px; background: var(--yellow); }
  .brand { position: absolute; left: 48px; top: 18px; display: flex; align-items: center; gap: 12px; }
  .brand-dot { width: 34px; height: 34px; border-radius: 50%; background: var(--logo); }
  .brand-name { font-family: "Montserrat", sans-serif; font-weight: 700; font-size: 38px; color: var(--logo); line-height: 1; }
  .address { position: absolute; left: 470px; top: 34px; font-size: 17px; font-weight: 600; color: var(--white); }
  .phone { position: absolute; right: 22px; top: 32px; display: flex; align-items: center; gap: 10px; font-size: 20px; font-weight: 600; color: var(--white); }

  .nav { position: absolute; left: 0; top: 86px; width: 1200px; height: 72px; background: var(--white); }
  .nav-link { position: absolute; top: 27px; font-size: 17px; font-weight: 500; color: var(--ink); }
  .btn { position: absolute; top: 19px; height: 39px; border-radius: 20px; display: flex; align-items: center; justify-content: center; font-size: 15px; font-weight: 500; }
  .btn-enroll { left: 818px; width: 164px; background: var(--blue-btn); color: var(--white); }
  .btn-call { left: 1001px; width: 161px; background: var(--lemon); color: var(--ink); }

  .hero { position: absolute; left: 0; top: 158px; width: 1200px; height: 757px; background: var(--yellow); overflow: hidden; }
  .hero-blob { position: absolute; left: -260px; top: -220px; width: 720px; height: 720px; border-radius: 50%; background: radial-gradient(circle at 55% 55%, #a9d0e6, var(--sky)); }
  .photo-left { position: absolute; left: 0; top: 200px; width: 450px; height: 557px; border-radius: 0 240px 0 0; background: linear-gradient(160deg, #f0d6d2, #e7b8bf 55%, #d9c3a8); }
  .photo-right { position: absolute; left: 740px; top: 120px; width: 460px; height: 637px; border-radius: 230px 0 0 0; background: linear-gradient(200deg, #f3c98a, #f5e6dc 50%, #e8b2a0); }

  .heart { position: absolute; left: 567px; top: 82px; }
  .hero-title { position: absolute; left: 0; top: 134px; width: 1200px; text-align: center; font-family: "Unbounded", sans-serif; font-weight: 800; font-size: 47px; line-height: 58px; color: var(--white); letter-spacing: 1px; }
  .hero-title .accent { color: var(--blue-text); }
  .discount { position: absolute; left: 379px; top: 387px; width: 441px; height: 58px; border-radius: 29px; background: var(--white); display: flex; align-items: center; justify-content: center; font-size: 22px; font-weight: 600; }
  .cta { position: absolute; left: 446px; top: 476px; width: 310px; height: 98px; border-radius: 49px; background: linear-gradient(90deg, var(--pink), var(--violet)); color: var(--white); display: flex; align-items: center; justify-content: center; text-align: center; font-size: 22px; font-weight: 500; line-height: 30px; }
</style>
</head>
<body>
  <header class="topbar">
    <div class="brand"><span class="brand-dot"></span><span class="brand-name">Тиливки</span></div>
    <div class="address">улица Берёзовая, 14, Ижевск</div>
    <div class="phone">
      <svg width="20" height="20" viewBox="0 0 24 24"><path fill="#fff" d="M6.6 10.8a15.1 15.1 0 0 0 6.6 6.6l2.2-2.2c.3-.3.7-.4 1-.2 1.1.4 2.3.6 3.6.6.6 0 1 .4 1 1V20c0 .6-.4 1-1 1A17 17 0 0 1 3 4c0-.6.4-1 1-1h3.5c.6 0 1 .4 1 1 0 1.3.2 2.5.6 3.6.1.3 0 .7-.2 1z"/></svg>
      <span>+7 (900) 555-27-31</span>
    </div>
  </header>

  <nav class="nav">
    <span class="nav-link" style="left:38px">Преимущества</span>
    <span class="nav-link" style="left:235px">Занятия</span>
    <span class="nav-link" style="left:377px">Педагоги</span>
    <span class="nav-link" style="left:528px">Отзывы</span>
    <span class="nav-link" style="left:668px">Контакты</span>
    <span class="btn btn-enroll">Записать ребенка</span>
    <span class="btn btn-call">Позвоните мне</span>
  </nav>

  <section class="hero">
    <div class="hero-blob"></div>
    <div class="photo-left" role="img" aria-label="Фотография: маленькая девочка в розовой кофте рисует за столом"></div>
    <div class="photo-right" role="img" aria-label="Фотография: улыбающаяся девочка показывает ладошки в разноцветной краске"></div>
    <svg class="heart" width="66" height="52" viewBox="0 0 66 52"><path fill="#fff" d="M33 52 6 26C-2 18-2 6 7 2c7-3 14 0 26 12C45 2 52-1 59 2c9 4 9 16 1 24z"/></svg>
    <h1 class="hero-title">Индивидуальные<br>и групповые занятия<br>для <span class="accent">детей 1-7 лет</span><br>в Ижевске</h1>
    <div class="discount">Скидка на первое занятие 50%</div>
    <div class="cta">Записаться<br>на первое занятие</div>
  </section>
</body>
</html>
```